CraneHollow - Business Card and Letterhead

After having received some fantastic submissions in our recent logo design project, I would now like to extend our branding to letterheads and business cards.
CraneHollow is a consulting service in the Construction Industry. We deal with both residential and commercial projects, and our clients include Architects, Builders, Tradespeople and Home Owners.
The designs should be simple and effective, convey personal service and professionalism, and display some level of creativity.
For both the business cards and letterhead, a white card stock will be used. This project is for business cards and letterheads only. Our new logo is attached for use.
The designs should incorporate our two main colours which are Blue (RGB 14,92,143) and Green (RGB 132,194,37).
For the time being, please submit all designs showing generic information including name, mobile number, email, postal address and website details. No fax number or physical address is required. I will provide our actual contact details once a final design has been selected.
I encourage you to interpret this brief in your own creative way, and look forward to some quality submissions.
Thanks!
Leo
CraneHollow.

```html
<!DOCTYPE html>
<html lang="en">
<head>
<meta charset="utf-8">
<title>CraneHollow Letterhead</title>
<link href="https://fonts.googleapis.com/css2?family=Arimo:wght@400;700&family=Open+Sans:wght@400&display=swap" rel="stylesheet">
<style>
  :root {
    --brand-blue: #1c6296;
    --brand-green: #86c342;
    --pale-green: #d0e6b4;
    --lavender: #a8b2d0;
    --frame-line: #333333;
    --label-grey: #777777;
    --text-grey: #666666;
    --footer-text: #111111;
    --paper: #ffffff;
  }
  html, body {
    margin: 0;
    padding: 0;
    width: 860px;
    height: 1200px;
    overflow: hidden;
    background: var(--paper);
  }
  .letterhead {
    position: relative;
    width: 860px;
    height: 1200px;
    background: var(--paper);
    overflow: hidden;
  }
  .frame-top, .frame-bottom {
    position: absolute;
    left: 18px;
    width: 825px;
    height: 1px;
    background: var(--frame-line);
  }
  .frame-top { top: 21px; }
  .frame-bottom { top: 1175px; }
  .band { position: absolute; }
  .band-blue { left: 18px; top: 21px; width: 31px; height: 1154px; background: var(--brand-blue); }
  .band-pale { left: 57px; top: 124px; width: 32px; height: 1051px; background: var(--pale-green); }
  .band-lavender-top { left: 770px; top: 21px; width: 32px; height: 47px; background: var(--lavender); }
  .band-lavender { left: 770px; top: 110px; width: 32px; height: 962px; background: var(--lavender); }
  .band-green-top { left: 810px; top: 21px; width: 33px; height: 47px; background: var(--brand-green); }
  .band-green { left: 810px; top: 110px; width: 33px; height: 1065px; background: var(--brand-green); }

  .brand {
    position: absolute;
    left: 57px;
    top: 40px;
    display: flex;
    align-items: center;
    gap: 14px;
  }
  .brand-mark {
    width: 50px;
    height: 50px;
    background: var(--brand-green);
  }
  .brand-name {
    font-family: "Arimo", Arial, sans-serif;
    font-weight: 700;
    font-size: 60px;
    line-height: 1;
    color: var(--brand-blue);
    letter-spacing: -0.5px;
  }

  .contact-email {
    position: absolute;
    left: 674px;
    top: 76px;
    font-family: "Arimo", Arial, sans-serif;
    line-height: 1.15;
  }
  .contact-email .label { font-weight: 700; font-size: 13px; color: var(--label-grey); }
  .contact-email .value { font-size: 14px; color: var(--text-grey); }

  .footer-field {
    position: absolute;
    left: 89px;
    top: 1080px;
    width: 721px;
    height: 95px;
    background: linear-gradient(180deg, var(--paper) 0%, var(--lavender) 35%, var(--pale-green) 70%);
  }
  .footer-address {
    position: absolute;
    left: 142px;
    top: 1138px;
    font-family: "Open Sans", Arial, sans-serif;
    font-style: normal;
    font-size: 12.5px;
    line-height: 15px;
    color: var(--footer-text);
  }
  .footer-contact {
    position: absolute;
    left: 560px;
    top: 1154px;
    font-family: "Open Sans", Arial, sans-serif;
    font-size: 11px;
    line-height: 15px;
    color: var(--footer-text);
    word-spacing: 1px;
  }
</style>
</head>
<body>
<div class="letterhead">
  <div class="frame-top"></div>
  <div class="band band-blue"></div>
  <div class="band band-pale"></div>
  <div class="band band-lavender-top"></div>
  <div class="band band-lavender"></div>
  <div class="band band-green-top"></div>
  <div class="band band-green"></div>

  <header class="brand">
    <span class="brand-mark"></span>
    <span class="brand-name">CraneHollow</span>
  </header>

  <div class="contact-email">
    <div class="label">EMAIL:</div>
    <div class="value">emailid@company.com</div>
  </div>

  <div class="footer-field" role="img" aria-label="Footer decoration area in lavender and pale green"></div>

  <address class="footer-address">
    Address: Dummy address dummy<br>
    00/00 dummy address, dummy,
  </address>
  <div class="footer-contact">Ph: 00 00000000 &nbsp;web: www.dddddddddd.com</div>

  <div class="frame-bottom"></div>
</div>
</body>
</html>
```